Integrated content management graphic

We are looking for a creative iteration for the attached file. We are currently in the process of renewing our branding and this graphic will be a center piece to our product marketing. Our website is www.brelvanto-docuhub.com for more information on products and company.
Future projects are available for designers submitting outstanding concepts and branding capability.

Target Market(s)

Audience is IT and anyone interested in integrating content management with their ERP/Accounting system.

Industry/Entity Type

Construction

Requirements
Must have
• The design must use the current color scheme associated with our website, yellow, black, grey. White can also be used. The design should be sleek.
Nice to have
• 3D Feel. The wheel could take on a stadium concept in 3d.

```html
<!DOCTYPE html>
<html lang="en">
<head>
<meta charset="utf-8">
<title>Brelvanto DocuHub – Integrated Content Management Wheel</title>
<link rel="stylesheet" href="https://fonts.googleapis.com/css2?family=Questrial&display=swap">
<style>
  :root {
    --page-bg: #ffffff;
    --rim-light: #f4f4f5;
    --rim-mid: #d6d6d8;
    --rim-dark: #a9a9ac;
    --ring-light: #fbfbfb;
    --ring-mid: #e2e2e4;
    --divider: #8e8e91;
    --label-fill: #ffffff;
    --label-edge: #8a8a8d;
    --hub-black: #1c1c1c;
    --brand-yellow: #f2c500;
  }
  html, body {
    margin: 0;
    padding: 0;
    width: 1200px;
    height: 1200px;
    overflow: hidden;
    background: var(--page-bg);
  }
  .wheel {
    display: block;
    width: 1200px;
    height: 1200px;
  }
  .wheel-label {
    font-family: "Questrial", "Century Gothic", sans-serif;
    fill: var(--label-fill);
    stroke: var(--label-edge);
    stroke-width: 1.2px;
    paint-order: stroke;
    letter-spacing: 1px;
  }
  .label-outer { font-size: 36px; }
  .label-middle { font-size: 33px; }
  .label-inner { font-size: 34px; }
  .hub-name {
    font-family: "Questrial", "Century Gothic", sans-serif;
    font-size: 62px;
    fill: var(--brand-yellow);
    letter-spacing: 1px;
  }
  .divider { stroke: var(--divider); stroke-width: 3; }
  .ring-edge { fill: none; stroke: var(--divider); stroke-width: 3; }
</style>
</head>
<body>
<svg class="wheel" viewBox="0 0 1200 1200" xmlns="http://www.w3.org/2000/svg" aria-label="Integrated content management wheel">
  <defs>
    <radialGradient id="halo" cx="50%" cy="50%" r="50%">
      <stop offset="88%" stop-color="#9a9a9d" stop-opacity="0.55"/>
      <stop offset="100%" stop-color="#ffffff" stop-opacity="0"/>
    </radialGradient>
    <radialGradient id="rim" cx="50%" cy="50%" r="50%">
      <stop offset="82%" stop-color="var(--rim-light)"/>
      <stop offset="92%" stop-color="var(--rim-mid)"/>
      <stop offset="100%" stop-color="var(--rim-dark)"/>
    </radialGradient>
    <radialGradient id="gap" cx="50%" cy="50%" r="50%">
      <stop offset="80%" stop-color="#ededee"/>
      <stop offset="90%" stop-color="#ffffff"/>
      <stop offset="100%" stop-color="#dcdcde"/>
    </radialGradient>
    <radialGradient id="middle-ring" cx="50%" cy="50%" r="50%">
      <stop offset="50%" stop-color="#d8d8da"/>
      <stop offset="75%" stop-color="var(--ring-light)"/>
      <stop offset="100%" stop-color="var(--ring-mid)"/>
    </radialGradient>
    <radialGradient id="inner-ring" cx="50%" cy="50%" r="50%">
      <stop offset="30%" stop-color="#ffffff"/>
      <stop offset="100%" stop-color="#cfcfd2"/>
    </radialGradient>
    <radialGradient id="hub" cx="40%" cy="35%" r="65%">
      <stop offset="0%" stop-color="#6a6a6a"/>
      <stop offset="55%" stop-color="var(--hub-black)"/>
      <stop offset="100%" stop-color="#000000"/>
    </radialGradient>

    <!-- outer band paths -->
    <path id="outer-top" d="M145,600 A455,455 0 0 1 1055,600"/>
    <path id="outer-bottom" d="M135,600 A465,465 0 0 0 1065,600"/>
    <path id="outer-left" d="M600,1025 A425,425 0 0 1 600,175"/>
    <path id="outer-right" d="M600,1068 A468,468 0 0 0 600,132"/>
    <!-- middle ring paths -->
    <path id="middle-top" d="M302,600 A298,298 0 0 1 898,600"/>
    <path id="middle-left" d="M600,890 A290,290 0 0 1 600,310"/>
    <path id="middle-right-1" d="M600,883 A283,283 0 0 0 600,317"/>
    <path id="middle-right-2" d="M600,928 A328,328 0 0 0 600,272"/>
    <path id="middle-bottom-1" d="M322,600 A278,278 0 0 0 878,600"/>
    <path id="middle-bottom-2" d="M282,600 A318,318 0 0 0 918,600"/>
    <!-- inner ring paths -->
    <path id="inner-top" d="M445,600 A155,155 0 0 1 755,600"/>
    <path id="inner-left" d="M600,750 A150,150 0 0 1 600,450"/>
    <path id="inner-right" d="M600,783 A183,183 0 0 0 600,417"/>
    <path id="inner-bottom" d="M430,600 A170,170 0 0 0 770,600"/>
  </defs>

  <g class="wheel-body">
    <circle class="shadow-halo" cx="600" cy="605" r="595" fill="url(#halo)"/>
    <circle class="outer-band" cx="600" cy="600" r="555" fill="url(#rim)"/>
    <circle class="gap-band" cx="600" cy="600" r="445" fill="url(#gap)"/>
    <circle class="middle-ring" cx="600" cy="600" r="395" fill="url(#middle-ring)"/>
    <circle class="ring-edge" cx="600" cy="600" r="395"/>
    <circle class="ring-edge" cx="600" cy="600" r="375" stroke-width="1.5"/>
    <circle class="inner-ring" cx="600" cy="600" r="240" fill="url(#inner-ring)"/>
    <circle class="ring-edge" cx="600" cy="600" r="240"/>
    <circle class="ring-edge" cx="600" cy="600" r="222" stroke-width="1.5"/>
  </g>

  <g class="dividers">
    <line class="divider" x1="230" y1="225" x2="335" y2="330"/>
    <line class="divider" x1="970" y1="225" x2="865" y2="330"/>
    <line class="divider" x1="230" y1="970" x2="335" y2="865"/>
    <line class="divider" x1="970" y1="970" x2="865" y2="865"/>
    <line class="divider" x1="335" y1="330" x2="535" y2="535"/>
    <line class="divider" x1="865" y1="330" x2="665" y2="535"/>
    <line class="divider" x1="335" y1="865" x2="535" y2="665"/>
    <line class="divider" x1="865" y1="865" x2="665" y2="665"/>
  </g>

  <g class="labels-outer">
    <text class="wheel-label label-outer"><textPath href="#outer-top" startOffset="50%" text-anchor="middle">Accounting</textPath></text>
    <text class="wheel-label label-outer"><textPath href="#outer-bottom" startOffset="50%" text-anchor="middle">Equipament Mgmt</textPath></text>
    <text class="wheel-label label-outer"><textPath href="#outer-left" startOffset="50%" text-anchor="middle">Property Mgmt</textPath></text>
    <text class="wheel-label label-outer"><textPath href="#outer-right" startOffset="50%" text-anchor="middle">Facilities Mgmt</textPath></text>
  </g>

  <g class="labels-middle">
    <text class="wheel-label label-middle"><textPath href="#middle-top" startOffset="50%" text-anchor="middle">Nimbus Office</textPath></text>
    <text class="wheel-label label-middle"><textPath href="#middle-left" startOffset="50%" text-anchor="middle">ShareCove</textPath></text>
    <text class="wheel-label label-middle"><textPath href="#middle-right-1" startOffset="50%" text-anchor="middle">Document</textPath></text>
    <text class="wheel-label label-middle"><textPath href="#middle-right-2" startOffset="50%" text-anchor="middle">Management</textPath></text>
    <text class="wheel-label label-middle"><textPath href="#middle-bottom-1" startOffset="50%" text-anchor="middle">Project</textPath></text>
    <text class="wheel-label label-middle"><textPath href="#middle-bottom-2" startOffset="50%" text-anchor="middle">Mgmt Software</textPath></text>
  </g>

  <g class="labels-inner">
    <text class="wheel-label label-inner"><textPath href="#inner-top" startOffset="50%" text-anchor="middle">Capture</textPath></text>
    <text class="wheel-label label-inner"><textPath href="#inner-left" startOffset="50%" text-anchor="middle">Archiving</textPath></text>
    <text class="wheel-label label-inner"><textPath href="#inner-right" startOffset="50%" text-anchor="middle">ERP</textPath></text>
    <text class="wheel-label label-inner"><textPath href="#inner-bottom" startOffset="50%" text-anchor="middle">Workflow</textPath></text>
  </g>

  <g class="hub">
    <circle cx="597" cy="600" r="80" fill="url(#hub)"/>
    <text class="hub-name" x="597" y="622" text-anchor="middle">BD</text>
  </g>
</svg>
</body>
</html>
```